Business Card Design

Like white and Blue with gold border

Industry/Entity Type

Business

Contact Information for Business Card

CLEARWAY TAX AND ACCOUNTING SERVICE
Registered Tax Agent
PO Box 815 or 167 Marlowe Street Rockhampton Q. 4700
Phone 07 41563092
Fax 07 41568417
clearwaytax@voskerhall.com
Senior Tax Preparer - MAREE COLWILL

Requirements
Must have
• on back of card should have - Appointment Date and time

```html
<!DOCTYPE html>
<html lang="en">
<head>
<meta charset="utf-8">
<title>Appointment Card</title>
<link rel="stylesheet" href="https://fonts.googleapis.com/css2?family=Roboto+Condensed:wght@400;700&display=swap">
<style>
  :root {
    --gold: #957b4e;
    --ink-blue: #2b4a8e;
    --paper: #ffffff;
  }
  * { margin: 0; padding: 0; box-sizing: border-box; }
  html, body {
    width: 1200px;
    height: 740px;
    overflow: hidden;
    background: var(--paper);
  }
  .card {
    position: relative;
    width: 1200px;
    height: 740px;
    background: var(--paper);
    border: 39px solid var(--gold);
    font-family: "Roboto Condensed", "Arial Narrow", sans-serif;
    color: var(--ink-blue);
  }
  .card-title {
    position: absolute;
    left: 0;
    right: 0;
    top: 150px;
    text-align: center;
    font-weight: 700;
    font-size: 52px;
    letter-spacing: -0.5px;
  }
  .field-label,
  .period-choice,
  .date-divider {
    position: absolute;
    font-weight: 400;
    font-size: 37px;
    line-height: 1;
  }
  .fill-line {
    position: absolute;
    height: 2px;
    background: var(--ink-blue);
  }
  .date-label  { left: 231px; top: 301px; }
  .date-line   { left: 350px; top: 338px; width: 486px; }
  .date-divider.first  { left: 509px; top: 301px; }
  .date-divider.second { left: 670px; top: 301px; }

  .time-label  { left: 231px; top: 413px; }
  .time-line   { left: 350px; top: 451px; width: 324px; }
  .period-choice { left: 683px; top: 413px; }
</style>
</head>
<body>
  <main class="card">
    <h1 class="card-title">Your Appointment</h1>

    <span class="field-label date-label">Date:</span>
    <span class="fill-line date-line"></span>
    <span class="date-divider first">/</span>
    <span class="date-divider second">/</span>

    <span class="field-label time-label">Time:</span>
    <span class="fill-line time-line"></span>
    <span class="period-choice">AM / PM</span>
  </main>
</body>
</html>
```